Business cards

Design business cards for our company. Just a straight, business like design with the logo, name, function and contact details

Target Market(s)

We are a innovative technological company active in water treatment

Industry/Entity Type

Water management

Contact Information for Business Card

Name, Function, email, telephone number, link to website

```html
<!DOCTYPE html>
<html lang="en">
<head>
<meta charset="utf-8">
<title>Tidewell Business Cards</title>
<link href="https://fonts.googleapis.com/css2?family=Montserrat:wght@500;700&family=Open+Sans:wght@300;400&display=swap" rel="stylesheet">
<style>
  :root {
    --brand-blue: #2f9ad6;
    --brand-blue-light: #49a9df;
    --card-white: #ffffff;
    --text-grey: #8a8a8a;
    --faint-grey: #f1f1f1;
    --bg-top: #cfcfcf;
    --bg-bottom: #a4a4a4;
  }
  * { margin: 0; padding: 0; box-sizing: border-box; }
  html, body { width: 1200px; height: 802px; overflow: hidden; }
  body {
    background: linear-gradient(180deg, var(--bg-top), var(--bg-bottom));
    font-family: "Open Sans", Arial, sans-serif;
    position: relative;
  }
  .card {
    position: absolute;
    top: 251px;
    width: 525px;
    height: 300px;
    border-radius: 26px;
    overflow: hidden;
    box-shadow: 0 14px 30px rgba(0,0,0,0.25);
  }
  .card--front { left: 50px; background: var(--card-white); }
  .card--back { left: 625px; background: var(--brand-blue); }

  .front__pattern {
    position: absolute;
    left: 0; bottom: 0;
    width: 300px; height: 200px;
    background: radial-gradient(ellipse at 30% 70%, var(--faint-grey), rgba(255,255,255,0) 70%);
  }
  .front__brand {
    position: absolute;
    top: 36px; right: 40px;
    display: flex; align-items: center; gap: 10px;
  }
  .brand-name {
    font-family: "Montserrat", Arial, sans-serif;
    font-weight: 500;
    color: var(--brand-blue);
    font-size: 30px;
    letter-spacing: 0.5px;
  }
  .brand-dot {
    width: 22px; height: 22px; border-radius: 50%;
    background: var(--brand-blue);
  }
  .brand-tagline {
    position: absolute;
    top: 78px; right: 72px;
    font-family: "Montserrat", Arial, sans-serif;
    font-size: 8px; letter-spacing: 1px;
    color: var(--text-grey);
  }
  .front__contact {
    position: absolute;
    top: 118px; left: 286px;
    color: var(--text-grey);
    font-weight: 300;
    font-size: 12.5px;
    line-height: 19px;
  }
  .contact__address { margin-bottom: 10px; }
  .contact__row { display: flex; align-items: center; gap: 8px; }
  .contact__row svg { width: 11px; height: 11px; flex: none; }
  .front__person {
    position: absolute;
    left: 0; bottom: 58px;
    display: flex; align-items: stretch;
  }
  .person__bar { width: 30px; background: var(--brand-blue); margin-right: 14px; }
  .person__name {
    font-family: "Montserrat", Arial, sans-serif;
    font-weight: 700; font-size: 19px;
    color: var(--brand-blue); letter-spacing: 1px;
  }
  .person__role { font-size: 14px; color: var(--text-grey); font-weight: 300; }

  .back__pattern {
    position: absolute; inset: 0;
    background: radial-gradient(ellipse at 75% 30%, var(--brand-blue-light), rgba(47,154,214,0) 65%);
  }
  .back__brand {
    position: absolute;
    top: 50%; left: 50%;
    transform: translate(-50%, -50%);
    text-align: center;
  }
  .back__brand .lockup { display: flex; align-items: center; gap: 16px; justify-content: center; }
  .back__brand .brand-name { color: var(--card-white); font-size: 54px; }
  .back__brand .brand-dot { width: 40px; height: 40px; background: var(--card-white); }
  .back__tagline {
    margin-top: 6px;
    font-family: "Montserrat", Arial, sans-serif;
    color: var(--card-white);
    font-size: 13px; letter-spacing: 2px;
  }
</style>
</head>
<body>
  <section class="card card--front">
    <div class="front__pattern" role="img" aria-label="Faint dotted bubble pattern"></div>
    <div class="front__brand">
      <span class="brand-name">Tidewell</span>
      <span class="brand-dot"></span>
    </div>
    <div class="brand-tagline">NANOBUBBLE TECHNOLOGY</div>

    <div class="front__contact">
      <div class="contact__address">17 Harbour Lane<br>Lakeport WT 4410</div>
      <div class="contact__row">
        <svg viewBox="0 0 12 12"><circle cx="6" cy="6" r="6" fill="#2f9ad6"/><path d="M4 3.2 5 4.6 4.5 5.3a4 4 0 0 0 2.2 2.2l.7-.5 1.4 1-.6 1A5 5 0 0 1 3 4l1-.8z" fill="#fff"/></svg>
        <span>555-014-2290</span>
      </div>
      <div class="contact__row">
        <svg viewBox="0 0 12 12"><circle cx="6" cy="6" r="6" fill="#2f9ad6"/><rect x="3" y="4" width="6" height="4.2" fill="none" stroke="#fff" stroke-width="0.8"/><path d="M3 4l3 2.3L9 4" fill="none" stroke="#fff" stroke-width="0.8"/></svg>
        <span>hello@tidewellwater.com</span>
      </div>
      <div class="contact__row">
        <svg viewBox="0 0 12 12"><circle cx="6" cy="6" r="6" fill="#2f9ad6"/><circle cx="6" cy="6" r="3" fill="none" stroke="#fff" stroke-width="0.8"/><path d="M3 6h6M6 3v6" stroke="#fff" stroke-width="0.7"/></svg>
        <span>www.tidewellwater.com</span>
      </div>
    </div>

    <div class="front__person">
      <div class="person__bar"></div>
      <div>
        <div class="person__name">DANA HOLLIS</div>
        <div class="person__role">CEO/Founder</div>
      </div>
    </div>
  </section>

  <section class="card card--back">
    <div class="back__pattern" role="img" aria-label="Soft pattern of light blue bubbles"></div>
    <div class="back__brand">
      <div class="lockup">
        <span class="brand-name">Tidewell</span>
        <span class="brand-dot"></span>
      </div>
      <div class="back__tagline">NANOBUBBLE TECHNOLOGY</div>
    </div>
  </section>
</body>
</html>
```